VELMARA IMAGING
Ultrasound Imaging Services
VELMARA IMAGING - Imaging
Creative Brief
Professional
Dorvan Tessliff
Ultrasound Diagnostic
5873 Calloway ridge ln Raleigh, NC 27614
dorvantessliff@mailvane.net
Concepts
Logo for mobile ultrasound

```html
<!DOCTYPE html>
<html lang="en">
<head>
<meta charset="utf-8">
<title>Velmara Imaging – Business Card</title>
<link href="https://fonts.googleapis.com/css2?family=Montserrat:wght@400;600;800&family=Open+Sans:wght@400;600&display=swap" rel="stylesheet">
<style>
  :root{
    --navy:#1c1f6e;
    --brand-blue:#2a6fd6;
    --sky:#3fb6e0;
    --sky-soft:#8fd6ef;
    --paper:#ffffff;
    --ink:#2b2b3a;
    --backdrop:#eceef2;
  }
  html,body{margin:0;padding:0;width:1200px;height:901px;overflow:hidden;background:var(--backdrop);}
  .stage{position:relative;width:1200px;height:901px;}
  .card{
    position:absolute;left:150px;top:193px;width:900px;height:514px;
    background:var(--paper);border-radius:40px;overflow:hidden;
    box-shadow:0 18px 40px rgba(20,25,60,.18);
    font-family:"Open Sans",Arial,sans-serif;
  }
  .card-waves{position:absolute;left:0;top:0;width:900px;height:514px;}
  .brand{position:absolute;left:70px;top:52px;}
  .brand-name{
    display:flex;align-items:center;gap:14px;
    font-family:"Montserrat",Arial,sans-serif;font-weight:800;font-size:58px;
    color:var(--brand-blue);letter-spacing:1px;line-height:1;
  }
  .brand-dot{width:22px;height:22px;border-radius:50%;background:var(--sky);}
  .brand-service{
    margin-top:8px;font-family:"Montserrat",Arial,sans-serif;font-weight:800;
    font-size:19px;color:var(--navy);letter-spacing:.5px;
  }
  .brand-tagline{
    margin-top:4px;font-family:"Montserrat",Arial,sans-serif;font-weight:600;
    font-size:12px;color:var(--sky);letter-spacing:2px;
  }
  .person{position:absolute;left:118px;top:190px;color:var(--ink);}
  .person-name{font-family:"Montserrat",Arial,sans-serif;font-weight:400;font-size:30px;letter-spacing:1px;line-height:1.3;}
  .person-role{font-size:19px;margin-top:2px;}
  .contacts{
    position:absolute;left:520px;top:314px;margin:0;padding:0;list-style:none;
    color:var(--paper);font-size:15px;
  }
  .contacts li{display:flex;align-items:center;gap:14px;height:36px;}
  .contact-icon{width:24px;height:24px;flex:none;}
</style>
</head>
<body>
<div class="stage">
  <div class="card">
    <svg class="card-waves" viewBox="0 0 900 514" aria-hidden="true">
      <path d="M0,295 C220,330 420,290 600,210 C720,175 820,160 900,165 L900,205 C800,200 700,215 600,252 C420,320 220,365 0,335 Z" fill="var(--sky)"/>
      <path d="M0,345 C220,375 420,330 600,262 C700,228 800,215 900,218 L900,228 C800,226 700,240 600,272 C420,340 220,388 0,360 Z" fill="var(--sky-soft)"/>
      <path d="M0,375 C220,400 400,330 600,270 C720,235 820,228 900,235 L900,514 L0,514 Z" fill="var(--navy)"/>
    </svg>

    <div class="brand">
      <div class="brand-name"><span class="brand-dot"></span>VELMARA</div>
      <div class="brand-service">IMAGING ULTRASOUND SERVICES</div>
      <div class="brand-tagline">ACCURATE FAST DIAGNOSIS</div>
    </div>

    <div class="person">
      <div class="person-name">DORVAN TESSLIFF</div>
      <div class="person-role">Managing Director</div>
    </div>

    <ul class="contacts">
      <li>
        <svg class="contact-icon" viewBox="0 0 26 26"><circle cx="13" cy="13" r="13" fill="#fff"/><path d="M9 7l3 3-2 2c1 2 2 3 4 4l2-2 3 3-2 2c-5 0-10-5-10-10z" fill="var(--navy)"/></svg>
        <span>919 555 0142</span>
      </li>
      <li>
        <svg class="contact-icon" viewBox="0 0 26 26"><circle cx="13" cy="13" r="13" fill="#fff"/><rect x="9" y="6" width="8" height="14" rx="1.5" fill="var(--navy)"/><circle cx="13" cy="17.5" r="1" fill="#fff"/></svg>
        <span>919 555 0187</span>
      </li>
      <li>
        <svg class="contact-icon" viewBox="0 0 26 26"><circle cx="13" cy="13" r="13" fill="#fff"/><rect x="7" y="9" width="12" height="8" fill="var(--navy)"/><path d="M7 9l6 5 6-5" stroke="#fff" stroke-width="1.2" fill="none"/></svg>
        <span>dorvantessliff@mailvane.net</span>
      </li>
      <li>
        <svg class="contact-icon" viewBox="0 0 26 26"><circle cx="13" cy="13" r="13" fill="#fff"/><circle cx="13" cy="13" r="6.5" fill="none" stroke="var(--navy)" stroke-width="1.5"/><path d="M6.5 13h13M13 6.5c-3 3.5-3 9.5 0 13M13 6.5c3 3.5 3 9.5 0 13" fill="none" stroke="var(--navy)" stroke-width="1.2"/></svg>
        <span>www.velmaraimaging.net</span>
      </li>
      <li>
        <svg class="contact-icon" viewBox="0 0 26 26"><circle cx="13" cy="13" r="13" fill="#fff"/><path d="M13 20s-5-5.5-5-9a5 5 0 0110 0c0 3.5-5 9-5 9z" fill="var(--navy)"/><circle cx="13" cy="11" r="1.8" fill="#fff"/></svg>
        <span>5873 Calloway ridge ln Raleigh, NC 27614</span>
      </li>
    </ul>
  </div>
</div>
</body>
</html>
```